Plakat-Design für einen mobilen Messestand
Zielgruppe
norvak ist Innovations-, Technologie- und Realisierungspartner für die digitale Transformation mit Spezialisierung auf Blockchain Technologien, Cyber Security und klassischen Softwareentwicklungsprojekten. Unsere Services umfassen Consulting, Entwicklungsleistungen und eigene Solutions.
Aufgabenstellung
Wir suchen ein Design für unseren neuen mobilen Messestand, bestehend aus einer Rückwand, zwei Roll-ups und einem Tresen (Stand 3x3, Druckdaten in den Uploads).
Da wir uns mitten in einem Rebranding befinden, ist noch kein Corporate Design definiert. Allerdings haben wir eine gewisse Vorstellung in welche Richtung das Design gehen soll.
**Rückwand**
Hier wollen wir die norvak Group als Holding in den Mittelpunk stellen. Neben dem norvak Group Logo soll auch unser Slogan „Shaping digital solutions“ sowie die drei Tochterfirmen (norvak experts, norvak consulting und norvak systems), zumindest subtil, abgebildet werden. Es soll ersichtlich werden, dass die norvak Group übergeordnet ist, es aber die drei Unterfirmen gibt.
Die Rückwand soll sehr clean gestaltet werden. Wir streben einen wertigen, modernen Look a la Computerunternehmen aus dem Silicon Valley ;-) an: schwarzer oder weißer Hintergrund, schwarze / weiße Schrift). Aufbrechen wollen wir das cleane schwarz/weiße Design durch knallige, leuchtende Farbakzente in grün, lila, blau (Farben der Tochterfirmen) - man könnte die Farbakzente beispielsweise im Arch, dem Symbol bei unserem Logo, oder durch „Farbwellen“ einbinden. (Inspiration in den Uplaods)
**Tresen**
Hier soll das Design der Rückwand harmonisch fortgeführt werden und das Logo der norvak Group abgebildet werden.
**2 Roll-ups** (Typ 'Basic')
Die Inhalte müssen noch definiert werden. Vermutlich wird auf dem einen Roll-up unsere Unternehmensstruktur und Ausrichtung genauer dargestellt und auf dem anderen das Thema Karriere bei norvak behandelt. Im ersten Schritt wäre ein Design sinnvoll, das harmonisch zur Rückwand passt und im zweiten Schritt flexibel mit Inhalten befüllt werden kann.
Deadline:
Wir benötigen die Designs sehr kurzfristig und würden uns erste Designvorschläge im Laufe dieser Woche wünschen, damit wir Anfang kommender Woche an das Fine Tuning und die Inh..

```html
<!DOCTYPE html>
<html lang="de">
<head>
<meta charset="utf-8">
<title>norvak – Messestand</title>
<link rel="stylesheet" href="https://fonts.googleapis.com/css2?family=Exo+2:wght@400;600&family=Share+Tech+Mono&display=swap">
<style>
  :root {
    --stage: #5d6267;
    --header-brand: #8a8f95;
    --header-slogan: #8d9197;
    --band: #f2f2f2;
    --white: #ffffff;
    --grey-text: #8c9096;
    --slogan: #7a7f86;
    --systems: #2f9a63;
    --experts: #6a4aa0;
    --consulting: #2c6fb5;
  }
  * { box-sizing: border-box; margin: 0; padding: 0; }
  html, body { width: 1200px; height: 552px; overflow: hidden; }
  body {
    position: relative;
    background: var(--stage);
    font-family: "Exo 2", sans-serif;
  }
  .header { position: absolute; left: 200px; top: 70px; width: 440px; }
  .header-brands { display: flex; gap: 26px; }
  .header-brands .brand { color: var(--header-brand); font-size: 18px; }
  .header-slogan {
    margin-top: 12px; font-family: "Share Tech Mono", monospace;
    font-size: 24px; color: var(--header-slogan); letter-spacing: 1px;
  }

  .piece { position: absolute; overflow: hidden; }
  .artwork { position: absolute; inset: 0; }

  .rollup-one { left: 120px; top: 190px; width: 100px; height: 330px; }
  .rollup-two { left: 320px; top: 170px; width: 110px; height: 340px; }
  .counter { left: 516px; top: 340px; width: 154px; height: 190px; }
  .backwall { left: 680px; top: 100px; width: 430px; height: 410px; }

  .rollup-one .artwork { background: linear-gradient(180deg, #0d1e3a 0%, #14294e 30%, #1a1c24 55%, #3a0c12 75%, #9a1522 100%); }
  .rollup-two .artwork { background: linear-gradient(180deg, #a5141f 0%, #4a0c14 28%, #15171c 55%, #0f2a52 80%, #1f5fa8 100%); }
  .counter .artwork { background: linear-gradient(180deg, #1b1d22 0%, #0e1014 100%); }
  .backwall .artwork { background: linear-gradient(90deg, #7a111c 0%, #2a0e14 30%, #0e1014 55%, #10213d 78%, #1a4a86 100%); }

  .logo {
    position: absolute; left: 0; right: 0; text-align: center;
    color: var(--white); font-weight: 600; letter-spacing: 1px;
  }
  .logo-mark {
    display: block; margin: 0 auto 8px; border-radius: 50%;
    border: 3px solid var(--white);
  }
  .rollup-one .logo { top: 40px; font-size: 26px; }
  .rollup-one .logo-mark { width: 44px; height: 44px; }
  .rollup-two .logo { top: 34px; font-size: 28px; }
  .rollup-two .logo-mark { width: 48px; height: 48px; }
  .counter .logo { top: 44px; font-size: 24px; color: var(--grey-text); }
  .backwall .logo { top: 70px; font-size: 46px; }
  .backwall .logo-mark { width: 70px; height: 70px; border-width: 4px; margin-bottom: 12px; }

  .band {
    position: absolute; left: 0; right: 0; background: var(--band);
    display: flex; flex-wrap: wrap; justify-content: center; align-content: center;
    column-gap: 8px; row-gap: 4px;
  }
  .rollup-one .band { top: 168px; height: 62px; padding: 0 4px; }
  .rollup-two .band { top: 176px; height: 64px; padding: 0 4px; }
  .counter .band { top: 96px; height: 30px; column-gap: 6px; }
  .backwall .band { top: 224px; height: 84px; column-gap: 30px; }

  .brand { font-weight: 600; line-height: 1; }
  .brand small { display: block; font-weight: 400; font-size: .7em; letter-spacing: .5px; }
  .brand.systems { color: var(--systems); }
  .brand.experts { color: var(--experts); }
  .brand.consulting { color: var(--consulting); }
  .rollup-one .brand, .rollup-two .brand { font-size: 12px; }
  .counter .brand { font-size: 7px; }
  .backwall .brand { font-size: 16px; }

  .band-slogan {
    width: 100%; text-align: center; font-family: "Share Tech Mono", monospace;
    color: var(--slogan); line-height: 1.1;
  }
  .counter .band-slogan { font-size: 7px; }
  .backwall .band-slogan { font-size: 24px; letter-spacing: 1px; margin-top: 4px; }
</style>
</head>
<body>
  <header class="header">
    <div class="header-brands">
      <span class="brand">norvak</span>
      <span class="brand">norvak</span>
      <span class="brand">norvak</span>
    </div>
    <p class="header-slogan">Shaping digital solutions</p>
  </header>

  <section class="piece rollup-one">
    <div class="artwork" role="img" aria-label="Abstraktes Netzwerkmuster aus Linien und Punkten, oben blau, unten rot leuchtend auf dunklem Grund"></div>
    <div class="logo"><span class="logo-mark"></span>norvak</div>
    <div class="band">
      <span class="brand systems">norvak<small>systems</small></span>
      <span class="brand experts">norvak<small>experts</small></span>
      <span class="brand consulting">norvak<small>consulting</small></span>
    </div>
  </section>

  <section class="piece rollup-two">
    <div class="artwork" role="img" aria-label="Abstraktes Netzwerkmuster aus Linien und Punkten, oben rot, unten blau leuchtend auf dunklem Grund"></div>
    <div class="logo"><span class="logo-mark"></span>norvak</div>
    <div class="band">
      <span class="brand systems">norvak<small>systems</small></span>
      <span class="brand experts">norvak<small>experts</small></span>
      <span class="brand consulting">norvak<small>consulting</small></span>
    </div>
  </section>

  <section class="piece counter">
    <div class="artwork" role="img" aria-label="Dunkle Tresenfläche mit dezentem Netzwerkmuster"></div>
    <div class="logo">norvak</div>
    <div class="band">
      <span class="brand systems">norvak</span>
      <span class="brand experts">norvak</span>
      <span class="brand consulting">norvak</span>
      <span class="band-slogan">Shaping digital solutions</span>
    </div>
  </section>

  <section class="piece backwall">
    <div class="artwork" role="img" aria-label="Abstraktes Netzwerkmuster, links rot, rechts blau leuchtend auf schwarzem Grund"></div>
    <div class="logo"><span class="logo-mark"></span>norvak</div>
    <div class="band">
      <span class="brand systems">norvak<small>systems</small></span>
      <span class="brand experts">norvak<small>experts</small></span>
      <span class="brand consulting">norvak<small>consulting</small></span>
      <span class="band-slogan">Shaping digital solutions</span>
    </div>
  </section>
</body>
</html>
```